Foldable creative restaurant menu

We require foldable restaurant menu to be placed on the each table, want it to look creative and modern with pages representing pictures of the dish not all dishes but few to represent what we do.Please get creative make sure its different, the colour should represent classy restaurant, not cheap and fast. The shape of the menu can be difference creative words must be easy to read and the logo must be in the menu here and there briefly.

Target Market(s)

Restaurant customers

Industry/Entity Type

Health And Wellness

Colors

Designer to choose colors to be used in the design.

Requirements
Must have
• foldable, must have good dish presentation pictures and must look modern and classy
Nice to have
• funky design and creative can be not just square foldable but can be interesting shape of menu.
Should not have
• boring plain spaces
• small writing
• dark pictures

```html
<!DOCTYPE html>
<html lang="en">
<head>
<meta charset="utf-8">
<title>Verdanta Restaurant – Breakfast Menu</title>
<link href="https://fonts.googleapis.com/css2?family=Dosis:wght@300;400;500&family=Oswald:wght@500&family=Montserrat:wght@300;400&display=swap" rel="stylesheet">
<style>
  :root{
    --paper:#f6f7f5;
    --ink:#2a2a2a;
    --text:#3c3c3c;
    --green:#7cc242;
    --frame:#555;
    --line:#1c1c1c;
  }
  *{box-sizing:border-box;margin:0;padding:0}
  html,body{width:1200px;height:849px;overflow:hidden;background:var(--paper)}
  .spread{position:relative;width:1200px;height:849px;background:
    repeating-linear-gradient(0deg,rgba(0,0,0,.012) 0 2px,transparent 2px 5px),
    repeating-linear-gradient(90deg,rgba(0,0,0,.012) 0 2px,transparent 2px 5px),var(--paper);
    font-family:"Dosis",sans-serif;color:var(--text)}
  .photo-breakfast{position:absolute;left:0;top:0;width:397px;height:849px;
    background:linear-gradient(180deg,#e9efe6 0%,#9a6a4a 25%,#c07a52 45%,#d98a3e 65%,#e8c98a 85%,#f4f2ee 100%)}
  .photo-acai{position:absolute;left:398px;top:118px;width:402px;height:630px;
    background:radial-gradient(ellipse at 50% 45%,#8e5a9a 0%,#a2679f 30%,#c28aa8 55%,#eee6ea 85%,#f6f4f4 100%)}
  .fold{position:absolute;top:0;height:849px;border-left:2px dotted var(--green)}
  .fold-a{left:397px}.fold-b{left:800px}
  .plant{position:absolute;left:880px;top:300px;width:300px;height:520px;
    background:radial-gradient(ellipse at 50% 50%,rgba(190,210,170,.22),rgba(190,210,170,0) 70%)}
  .menu-card{position:absolute;left:60px;top:86px;width:272px;height:708px;
    border:2px dotted var(--green);background:rgba(255,255,255,.94)}
  .menu-card h2{position:absolute;left:22px;top:14px;font-family:"Oswald",sans-serif;
    font-weight:500;font-size:27px;color:var(--green);letter-spacing:-.5px;transform:scaleX(.85);transform-origin:left}
  .item{position:absolute;left:22px;width:236px;font-size:11.3px;line-height:14.5px;font-weight:300}
  .item .name{font-weight:500;color:var(--ink);text-transform:uppercase;letter-spacing:.2px}
  .item p{margin-top:1px}
  .acai-box{position:absolute;left:13px;top:125px;width:246px;height:208px;border:1px solid var(--frame);
    padding:8px 0 0 9px;font-size:11.3px;line-height:14.5px;font-weight:300}
  .acai-box .title{font-family:"Oswald",sans-serif;font-weight:400;font-size:15px;color:var(--ink);transform:scaleX(.85);transform-origin:left;display:inline-block}
  .acai-box .option{margin-top:10px;width:230px}
  .brand{position:absolute;left:840px;top:206px;color:var(--line)}
  .brand .name{font-family:"Montserrat",sans-serif;font-weight:300;font-size:56px;letter-spacing:3px}
  .brand .tag{font-family:"Montserrat",sans-serif;font-weight:400;font-size:25px;letter-spacing:6.5px;margin-top:6px}
  .zigzag{position:absolute;left:0;top:0}
</style>
</head>
<body>
<main class="spread">
  <div class="photo-breakfast" role="img" aria-label="Photo of a full breakfast plate with poached eggs, spinach, bacon, mushrooms and toast"></div>
  <div class="photo-acai" role="img" aria-label="Photo of an acai bowl topped with strawberries, banana, kiwi, granola and chia seeds"></div>
  <div class="plant" role="img" aria-label="Faint leafy plant silhouette"></div>
  <div class="fold fold-a"></div>
  <div class="fold fold-b"></div>

  <svg class="zigzag" width="1200" height="849" viewBox="0 0 1200 849" fill="none" stroke="var(--line)" stroke-width="1">
    <polyline points="0,104 32,0"/>
    <polyline points="0,740 32,849"/>
    <polyline points="365,0 397,88 429,0"/>
    <polyline points="365,849 397,740 429,849"/>
    <polyline points="768,0 800,104 832,0"/>
    <polyline points="768,849 800,740 832,849"/>
    <polyline points="1168,0 1200,104"/>
    <polyline points="1168,849 1200,740"/>
  </svg>

  <section class="menu-card">
    <h2>BREAKFAST</h2>
    <div class="item" style="top:54px"><span class="name">Big Verdanta Breakfast&nbsp; 19</span>
      <p>Choose from sourdough OR Turkish served with eggs, bacon, chipolata's, hash brown, spinach, tomato &amp; mushroom</p></div>
    <div class="acai-box">
      <span class="title">ACAI BOWL</span>&nbsp; 13<br>Choice of:
      <p class="option">(1) Zesty Detox - Acai pure, Frozen Raspberries, Banana, Apple Juice with garnish on</p>
      <p class="option">(2) Antioxidant - Acai pure, Frozen Berries, Avocado, coconut water with garnish on to</p>
      <p class="option">(3) Tropical Fest - Acai pure OR energy, Frozen Mango, Coconut Water with garnish on top</p>
      <p class="option">(4) Cocolicious - Tropica Coconut, Banana, Coconut Water with garnish on top</p>
    </div>
    <div class="item" style="top:345px"><span class="name">Avocado Smash - V GF&nbsp; 13</span>
      <p>Feta, spinach &amp; avocado served on the sourdough</p></div>
    <div class="item" style="top:399px"><span class="name">Eggs Benedict&nbsp; 10</span>
      <p>Poached eggs, English muffin, sautéed baby spinach served with hollandaise</p></div>
    <div class="item" style="top:452px"><span class="name">Egg &amp; Bacon Roll&nbsp; 10</span></div>
    <div class="item" style="top:477px"><span class="name">Add On's</span>
      <p>Spinach 2.00, Mushroom 2.00, &nbsp;Egg 2.00, Cheese 2.00 Avocado 3.00, Bacon 3.00, Ham 3.00, Chipolata's 3.00, Smoked salmon 5.00,</p></div>
    <div class="item" style="top:545px"><span class="name">Bruschetta&nbsp;&nbsp; 12</span>
      <p>Toast served with a mix of tangy tomatoes, basil, red onion and garlic &amp; with Feta cheese and Balsamic Italian dressing as garnish.</p></div>
    <div class="item" style="top:613px"><span class="name">7-Seed Breakfast&nbsp;&nbsp; 10</span>
      <p>Deliciously toasted seven-seed Low Gluten bread topped with pesto sauce; served with ham, scrambled egg, four- leaf salad, sundried &amp; cherry tomatoes and feta cheese</p></div>
  </section>

  <header class="brand">
    <div class="name">Verdanta</div>
    <div class="tag">RESTAURANT</div>
  </header>
</main>
</body>
</html>
```